Innovative Funky Australian Start Up - HR & Recruitment

We would like a brochure for our company "Crewmark". We provide affordable HR & Recruitment support for Small to Medium businesses.
We like a simple, fresh, crisp, clean look. Nothing overly complicated.
Target market is Small and medium businesses with 2-50 employees, this could be in IT, Accounting, Construction, Marketing or a Engineering, so really trying to appeal to all industries. We don’t want to come across as too high end corporate – more everyday professional. I’d say our target client is probably late 30’s to late 40’s owner or general manager
Our website is - www.crewmarkhq.com.au

Target Market(s)

Small and medium size business's.
Business owners.
Multiple industries

Industry/Entity Type

It Company

Font styles to use
Sans Serif

```html
<!DOCTYPE html>
<html lang="en">
<head>
<meta charset="utf-8">
<title>Crewmark – HR &amp; Recruitment Brochure</title>
<link rel="stylesheet" href="https://fonts.googleapis.com/css2?family=Nunito+Sans:ital,wght@0,300;0,400;0,600;0,700;0,800;1,400&display=swap">
<style>
:root{
  --backdrop:#3a3b3d;
  --navy:#1d5e96;
  --deep:#14497a;
  --sky:#1fa2e8;
  --bright:#2db0f2;
  --ink:#2c3a48;
  --paper:#ffffff;
  --soft:#dcecf8;
}
*{box-sizing:border-box;margin:0;padding:0}
html,body{width:1200px;height:880px;overflow:hidden}
body{background:var(--backdrop);font-family:"Nunito Sans",Arial,sans-serif;color:var(--paper);position:relative}
.spread{position:absolute;width:560px;height:395px;overflow:hidden;background:var(--paper)}
.spread--cover{left:30px;top:30px}
.spread--about{left:610px;top:30px}
.spread--services{left:30px;top:455px}
.spread--policies{left:610px;top:455px}
.art{position:absolute;left:0;top:0;width:560px;height:395px}
.t{position:absolute}
.small{font-size:4.7px;line-height:1.35;font-weight:400}
.small p{margin-bottom:3px}
.small b{font-weight:700}

/* cover */
.quote{left:166px;top:16px;width:86px;text-align:center;font-size:4.4px;line-height:1.4}
.quote-sign{left:166px;top:150px;width:86px;text-align:center;font-size:7px;font-style:italic;line-height:1.5}
.cover-invite{left:70px;top:306px;width:176px;text-align:right;font-size:8px;line-height:1.4;font-weight:400}
.contact{left:60px;top:345px;font-size:5.6px;line-height:1.75;color:var(--ink)}
.contact span{display:inline-block;width:9px;color:var(--sky);font-weight:700}
.hr-title{left:315px;top:280px;line-height:1}
.hr-title .your{font-size:19px;font-weight:300;display:block}
.hr-title .team{font-size:34px;font-weight:800}
.hr-title .team em{font-style:normal;font-weight:300;font-size:24px}
.brand{left:402px;top:340px;display:flex;align-items:center;gap:6px;color:var(--ink);font-size:16px;font-weight:600}
.brand i{display:block;width:16px;height:16px;border-radius:50%;background:var(--sky)}
.footer-web{top:381px;font-size:6px;color:var(--paper)}

/* headings */
.band-title{left:20px;top:11.5px;font-size:7.5px;font-weight:600;letter-spacing:.3px}
.section-title{font-size:7.6px;font-weight:600;letter-spacing:.2px}
.list{list-style:none;font-size:6px;line-height:1.65}
.list li{position:relative;padding-left:11px}
.list li::before{content:"";position:absolute;left:0;top:2.2px;width:6px;height:6px;border-radius:50%;background:var(--paper);box-shadow:inset 0 0 0 1.6px var(--sky)}
.list b{font-weight:700}
.ticks{list-style:none;font-size:6px;line-height:1.75}
.ticks li::before{content:"✓";margin-right:3px;font-weight:700}
.values{display:grid;grid-template-columns:118px 140px}
.big-title{font-size:15px;font-weight:400}
.big-title b{font-weight:800}
.assist{list-style:none;font-size:4.8px;line-height:1.95;display:grid;grid-template-columns:124px 120px}
.assist li{position:relative;padding-left:9px}
.assist li.wide{grid-column:1 / 3}
.assist li::before{content:"";position:absolute;left:0;top:2px;width:4.6px;height:4.6px;border-radius:50%;background:var(--paper);box-shadow:inset 0 0 0 1.3px var(--sky)}
.policy-list{font-size:5.2px;line-height:1.8}
.policy-list li::before{top:1.6px;width:5px;height:5px}
</style>
</head>
<body>

<!-- Spread 1: outer cover -->
<section class="spread spread--cover" aria-label="Brochure cover spread">
  <svg class="art" viewBox="0 0 560 395" aria-hidden="false">
    <defs>
      <linearGradient id="officeMan" x1="0" y1="0" x2="1" y2="1">
        <stop offset="0" stop-color="#e9e6df"/><stop offset="1" stop-color="#8fa9c4"/>
      </linearGradient>
      <linearGradient id="cafeWoman" x1="0" y1="0" x2="1" y2="1">
        <stop offset="0" stop-color="#a07a58"/><stop offset="1" stop-color="#d8d0c6"/>
      </linearGradient>
    </defs>
    <g role="img" aria-label="Photo of a smiling businessman in a blue shirt with arms crossed">
      <rect x="0" y="0" width="280" height="300" fill="url(#officeMan)"/>
    </g>
    <g role="img" aria-label="Photo of a smiling café owner in a check shirt behind her counter">
      <rect x="280" y="0" width="280" height="300" fill="url(#cafeWoman)"/>
    </g>
    <rect x="163" y="0" width="92" height="205" fill="#1fa2e8" opacity=".86"/>
    <polygon points="0,330 280,222 560,300 560,330 280,378 0,340" fill="#1fa2e8"/>
    <polygon points="0,330 280,222 280,378 0,340" fill="#1b8fd6"/>
    <polygon points="0,342 280,378 0,378" fill="#ffffff"/>
    <polygon points="280,378 560,332 560,378" fill="#ffffff"/>
    <line x1="0" y1="340" x2="280" y2="377" stroke="#2c3a48" stroke-width="3"/>
    <line x1="280" y1="377" x2="560" y2="330" stroke="#14497a" stroke-width="3"/>
    <rect x="0" y="378" width="560" height="17" fill="#2c3a48"/>
    <line x1="0" y1="378.5" x2="560" y2="378.5" stroke="#1fa2e8" stroke-width="1"/>
  </svg>
  <p class="t quote">“I first contacted Crewmark when my staff jumped from 2-6 employees when we won a big client. It was then I realised I had to make sure I had proper employment contracts and was paying people correctly. Without going into details – I was majorly stuffing up! Thankfully Crewmark sorted everything out for me, implemented a proper HR system and had my new staff properly onboarded within a week for less than $800. I couldn't believe it! A lifesaver! Now I use them for any staff issues or recruitment that pops up.”</p>
  <p class="t quote-sign">Director –<br>Perth Small Business</p>
  <p class="t cover-invite">Please contact us to<br>discuss how Crewmark can assist<br>your organisation.</p>
  <div class="t contact">
    <div><span>✆</span>1300 555 019</div>
    <div><span>✉</span>info@crewmarkhq.com.au</div>
    <div><span>⚲</span>Perth | Melbourne | Sydney | Brisbane | Adelaide</div>
  </div>
  <h1 class="t hr-title"><span class="your">YOUR</span><span class="team">HR <em>TEAM.</em></span></h1>
  <div class="t brand"><i></i>Crewmark</div>
  <p class="t footer-web" style="left:62px">⊕ www.crewmarkhq.com.au</p>
  <p class="t footer-web" style="left:432px">⊕ www.crewmarkhq.com.au</p>
</section>

<!-- Spread 2: about us / recruitment -->
<section class="spread spread--about" aria-label="About us and recruitment spread">
  <svg class="art" viewBox="0 0 560 395">
    <defs>
      <linearGradient id="studyPhoto" x1="0" y1="0" x2="1" y2="1">
        <stop offset="0" stop-color="#cfc6b8"/><stop offset="1" stop-color="#7a6c60"/>
      </linearGradient>
      <linearGradient id="officePhoto" x1="0" y1="0" x2="1" y2="1">
        <stop offset="0" stop-color="#dfe3e4"/><stop offset="1" stop-color="#b88b7c"/>
      </linearGradient>
    </defs>
    <rect x="0" y="0" width="280" height="395" fill="#1d5e96"/>
    <polygon points="0,10 176,10 170,22 0,22" fill="#14497a"/>
    <polygon points="180,10 280,10 280,22 174,22" fill="#1fa2e8"/>
    <g role="img" aria-label="Photo of a woman working on a laptop beside a boy drawing at a desk">
      <polygon points="0,268 280,250 280,395 0,395" fill="url(#studyPhoto)"/>
    </g>
    <polygon points="0,268 100,300 0,335" fill="#1fa2e8"/>
    <g role="img" aria-label="Photo of a smiling man with crossed arms in a busy open-plan office">
      <rect x="280" y="0" width="280" height="230" fill="url(#officePhoto)"/>
    </g>
    <polygon points="280,215 560,165 560,395 280,395" fill="#1766ab"/>
    <polygon points="280,215 560,165 560,180 280,234" fill="#1fa2e8"/>
  </svg>
  <h2 class="t band-title">ABOUT US</h2>
  <div class="t small" style="left:20px;top:29px;width:245px">
    <p>Crewmark is a Human Resources &amp; Recruitment consultancy focussed on providing high quality, cost effective people solutions to Australian businesses.</p>
    <p>With a unique business model and using a team of specialists we are able to offer the best priced services across the country, backed by incredible quality of service and a genuine desire to support business growth and affect positive change within our community.</p>
    <p>Our clients range from global corporates, to small businesses operating from home. Whatever your needs and for whatever direction you're heading, we will be with you every step of the way.</p>
    <p>Working with Crewmark means you've got the best in the business, at the best price, and you're helping to drive community change whilst also making positive steps forward for your business.</p>
  </div>
  <h3 class="t section-title" style="left:20px;top:112px">WHAT WE DO</h3>
  <ul class="t list" style="left:20px;top:124px">
    <li><b>Recruitment.</b> Fixed low rates.</li>
    <li><b>HR Services</b> – Consulting, onsite &amp; phone support.</li>
    <li><b>Contracts,</b> Policies &amp; Procedures.</li>
    <li><b>Restructures,</b> Redundancy Management</li>
    <li><b>Dismissals,</b> Fairwork representation</li>
    <li><b>Project Support</b> – bulk recruitment drives, HR admin.</li>
  </ul>
  <h3 class="t section-title" style="left:20px;top:198px">OUR VALUES</h3>
  <ul class="t ticks values" style="left:20px;top:210px">
    <li>Diversity, Equal Opportunity</li><li>Gender equality, Flexibility for families</li>
    <li>Mature aged employment</li><li>Women in leadership</li>
    <li>Cultural awareness &amp; diversity</li><li>Indigenous employment</li>
  </ul>
  <h3 class="t section-title" style="left:412px;top:238px;font-size:8.5px">RECRUITMENT</h3>
  <ul class="t list" style="left:412px;top:251px;font-size:5.8px">
    <li>Australia's best-priced Recruitment.</li>
    <li>Fixed rate prices. No hidden fees.</li>
    <li>Dedicated, reliable Consultants</li>
    <li>Any industry, any job position</li>
  </ul>
  <div class="t small" style="left:295px;top:297px;width:250px;font-size:4.3px">
    <p>At Crewmark we have a real passion for people and are committed to ensuring the best possible long term outcomes for all our clients.</p>
    <p>We're just like you, we understand that people are a company's biggest asset, also often its biggest expense, and in any business – time is money.</p>
    <p>That's why our quick, easy and affordable recruitment model is so popular in today's demanding market. We let you concentrate on running your business, whilst supplying you with the people you need.</p>
    <p>We aren't just a Recruitment Agency, we are your dedicated “People Managers”, meaning we are there to offer you HR guidance and support when required as well.</p>
    <p>You will have a dedicated Recruiter who understands your needs, your business and the culture. We also help managers with interviewing tips and understanding how not just to attract the best talent, but also to retain, engage and develop your employees long term.</p>
    <p><b>Crewmark are an open book, to see our pricing visit our website www.crewmarkhq.com.au</b></p>
  </div>
</section>

<!-- Spread 3: HR services -->
<section class="spread spread--services" aria-label="HR services spread">
  <svg class="art" viewBox="0 0 560 395">
    <defs>
      <linearGradient id="consultPhoto" x1="0" y1="0" x2="1" y2="1">
        <stop offset="0" stop-color="#efe9de"/><stop offset="1" stop-color="#b59a7c"/>
      </linearGradient>
      <linearGradient id="meetingPhoto" x1="0" y1="0" x2="1" y2="1">
        <stop offset="0" stop-color="#e6ddd0"/><stop offset="1" stop-color="#8aa3b8"/>
      </linearGradient>
    </defs>
    <rect x="0" y="0" width="560" height="395" fill="#1d5e96"/>
    <g role="img" aria-label="Photo of a smiling businesswoman in a beige blazer in an office">
      <polygon points="0,0 280,0 280,198 0,240" fill="url(#consultPhoto)"/>
    </g>
    <polygon points="140,219 280,198 280,203 140,224" fill="#ffffff"/>
    <polygon points="0,240 150,272 0,294" fill="#1fa2e8"/>
    <g role="img" aria-label="Photo of a presenter leading a team meeting at a whiteboard">
      <polygon points="280,160 560,118 560,395 280,395" fill="url(#meetingPhoto)"/>
    </g>
    <polygon points="400,142 560,118 560,123 400,147" fill="#ffffff"/>
    <polygon points="280,142 400,160 280,186" fill="#1fa2e8"/>
  </svg>
  <h2 class="t big-title" style="right:292px;top:268px">HR <b>SERVICES</b></h2>
  <div class="t small" style="left:20px;top:292px;width:250px;font-size:4.4px">
    <p><b>RETAINED, OUTSOURCED HR.</b> Let us be your dedicated, regular HR support, whether that's for two days a week or two hours a month. We're there as you need us in person or over the phone. We offer monthly memberships and regular internal &amp; external support of related roles.</p>
    <p><b>HR CONSULTING.</b> Whether it's workplace investigations, dismissal or remuneration &amp; benefits advice, performance management, manager training or working with your business to build high performance teams, we have an option to suit your business.</p>
    <p><b>ONSITE SUPPORT.</b> Our experienced HR &amp; Recruitment Consultants are available for onsite support for project delivery, peak workloads, recruitment campaigns and restructures.</p>
    <p><b>HR for SME's &amp; START UPS.</b> We provide you with all the HR Documentation that your business needs, so you can be confident that you are meeting your legal requirements. This includes employment contracts, policies &amp; procedures, new employee forms, induction checklists &amp; more.</p>
  </div>
  <h2 class="t section-title" style="left:302px;top:18px;font-size:9.5px;font-weight:400">WE ASSIST CLIENTS WITH:</h2>
  <ul class="t assist" style="left:302px;top:35px">
    <li class="wide">Review of employment contracts</li>
    <li class="wide">Workplace investigations including bullying and misconduct</li>
    <li class="wide">Managing people related issues or aggrieved employees</li>
    <li>Disciplinary advice and procedures</li><li>Termination or Redundancy advice</li>
    <li>FairWork and unfair dismissal assistance</li><li>Creation of Job descriptions</li>
    <li>Staff Training &amp; Induction processes</li><li>Interview Techniques for Managers</li>
    <li class="wide">Creation of Performance Management programs</li>
    <li>Performance improvement procedures</li><li>Remuneration &amp; Benefits Advice</li>
    <li>Talent Acquisition &amp; Employee Retention</li><li>Managing Organisational Change</li>
  </ul>
</section>

<!-- Spread 4: policies / why we're different -->
<section class="spread spread--policies" aria-label="Templates and why we're different spread">
  <svg class="art" viewBox="0 0 560 395">
    <defs>
      <linearGradient id="filesPhoto" x1="0" y1="0" x2="1" y2="1">
        <stop offset="0" stop-color="#f4f4f2"/><stop offset="1" stop-color="#c9cfd4"/>
      </linearGradient>
      <linearGradient id="teamPhoto" x1="0" y1="0" x2="1" y2="1">
        <stop offset="0" stop-color="#dfe2e2"/><stop offset="1" stop-color="#6d7680"/>
      </linearGradient>
    </defs>
    <rect x="0" y="0" width="560" height="395" fill="#1d5e96"/>
    <g role="img" aria-label="Photo of a white office shelf with binders, paperwork stacks and a plant">
      <polygon points="0,240 280,205 280,395 0,395" fill="url(#filesPhoto)"/>
    </g>
    <polygon points="120,225 280,205 280,210 120,230" fill="#ffffff"/>
    <polygon points="0,240 130,265 0,292" fill="#1fa2e8"/>
    <g role="img" aria-label="Photo of a smiling young businesswoman in an open-plan office">
      <polygon points="280,0 560,0 560,125 280,190" fill="url(#teamPhoto)"/>
    </g>
    <polygon points="280,150 420,162 280,196" fill="#1fa2e8"/>
  </svg>
  <h2 class="t section-title" style="left:20px;top:16px;font-weight:400;font-size:7.6px">Crewmark Provide Comprehensive Templates &amp; Customised:</h2>
  <p class="t small" style="left:20px;top:29px;font-size:4.6px">Contracts of Employment for Full time, Part time and &amp; Casual employees</p>
  <h3 class="t section-title" style="left:20px;top:43px;font-weight:400;font-size:6.6px">Essential Policies &amp; Procedures such as:</h3>
  <ul class="t list policy-list" style="left:20px;top:55px">
    <li>Use of IT, Internet, Email &amp; Social Media</li>
    <li>Code of Conduct</li>
    <li>Drug &amp; Alcohol</li>
    <li>Occupational Health &amp; Safety</li>
    <li>Bullying, Sexual Harassment</li>
    <li>Attendance &amp; Punctuality</li>
    <li>Leave</li>
    <li>Equal Opportunity of Employment, Diversity</li>
    <li>Corrective Action &amp; Discipline</li>
  </ul>
  <p class="t" style="left:20px;top:148px;width:220px;font-size:5.6px;line-height:1.4">Recruitment &amp; New Employee Documents such as interview guides, reference check forms and induction checklists.</p>
  <p class="t" style="left:20px;top:170px;width:220px;font-size:5.6px;line-height:1.4">Staff Management Documentations including probation, warning, termination &amp; redundancy letters.</p>
  <h2 class="t" style="left:302px;top:200px;font-size:10.5px;font-weight:400">Why We're Different</h2>
  <div class="t small" style="left:302px;top:220px;width:242px;font-size:4.3px">
    <p>We're just like you, and we want to see your business grow, develop and be successful. We want to really get to know you, your business and your staff, to assist in managing any issues that arise, and to help you develop engaged, productive teams.</p>
    <p>Our team is made up of highly experienced, educated, capable and exceptionally dedicated people, predominately working Mums. Each member of our team has over 12 years' experience within highly technical, demanding corporate careers.</p>
    <p>You see, we believe in how capable and driven working parents are, and we're tapping into that huge resource of experienced people who simply want the flexibility to work around the needs of their family.</p>
    <p>We believe that through our hiring processes, and how we manage people – we can change the world. We promote our company values at every opportunity, because we know values and core beliefs are also what drive productivity and success in business as well.</p>
  </div>
  <p class="t" style="left:302px;top:324px;font-size:5.6px">Our clients say <span style="font-size:8px">We:</span></p>
  <ul class="t ticks" style="left:302px;top:336px;font-size:4.8px;line-height:1.85">
    <li>Are Transparent, Ethical</li>
    <li>Knowledgeable, Down to Earth</li>
    <li>Committed, Personalised</li>
    <li>Fast, Flexible</li>
    <li>Have Exceptional Service &amp; Quality</li>
  </ul>
</section>

</body>
</html>
```